Stationery Design For Specialist London law firm

We have merged two firms of London lawyers to create a new firm with a new name.

The new firms name is KR Holloway. We would like to include the description Solicitors and Advocates in the design.

We need a new design for our headed paper, business cards compliment slips etc.

The image we wish to project is fresh but not gimmicky - reliable and strong but not stuffy.

We have no strong views on font or colour this really is pretty much a blank page.

Our preference is for the name to be at the top of the page

Target Market(s)

Our clients who are individuals rather than corporate and other lawyers

Industry/Entity Type

Law Firm

Requirements
Should not have
• Legal images eg scales of justice etc

Obviously nothing childish or gimmicky

```html
<!DOCTYPE html>
<html lang="en">
<head>
<meta charset="utf-8">
<title>KR Holloway – Solicitors and Advocates</title>
<link rel="stylesheet" href="https://fonts.googleapis.com/css2?family=Arvo:wght@700&family=Courier+Prime:wght@700&family=EB+Garamond:wght@400;500&display=swap">
<style>
  :root {
    --paper: #ffffff;
    --banner: #6f6b8e;
    --banner-edge: #cfcdd8;
    --ink-light: #ffffff;
    --gold: #c9a23a;
    --ink-dark: #1c1c1c;
    --art-slate-a: #5d6070;
    --art-slate-b: #4c4f60;
    --art-olive-a: #9a9a62;
    --art-olive-b: #8a8458;
  }
  html, body {
    margin: 0;
    padding: 0;
    width: 1200px;
    height: 840px;
    overflow: hidden;
    background: var(--paper);
  }
  .letterhead {
    position: relative;
    width: 1200px;
    height: 840px;
    background: var(--paper);
  }
  .banner {
    position: absolute;
    inset: 0;
    width: 1200px;
    height: 840px;
  }
  .banner-shape {
    fill: var(--banner);
    stroke: var(--banner-edge);
    stroke-width: 4;
  }
  .mortarboard-art {
    position: absolute;
    left: 240px;
    top: 60px;
    width: 396px;
    height: 276px;
    background: linear-gradient(160deg, var(--art-slate-a), var(--art-slate-b));
  }
  .hourglass-art {
    position: absolute;
    left: 990px;
    top: 372px;
    width: 68px;
    height: 152px;
    background: linear-gradient(180deg, var(--art-olive-a), var(--art-olive-b));
  }
  .practice-areas {
    position: absolute;
    left: 720px;
    top: 150px;
    width: 360px;
    margin: 0;
    padding: 0;
    list-style: none;
    text-align: center;
    font-family: "EB Garamond", serif;
    font-size: 38px;
    line-height: 52px;
    color: var(--ink-light);
  }
  .firm-name {
    position: absolute;
    left: 84px;
    top: 362px;
    margin: 0;
    font-family: "Arvo", serif;
    font-weight: 700;
    font-size: 100px;
    line-height: 1;
    letter-spacing: 2px;
    color: var(--ink-light);
    white-space: nowrap;
  }
  .firm-descriptor {
    position: absolute;
    left: 104px;
    top: 490px;
    margin: 0;
    font-family: "Courier Prime", monospace;
    font-weight: 700;
    font-size: 54px;
    line-height: 1;
    color: var(--gold);
    white-space: nowrap;
  }
  .contact {
    position: absolute;
    left: 236px;
    top: 572px;
    width: 600px;
    margin: 0;
    text-align: center;
    font-family: "EB Garamond", serif;
    font-weight: 500;
    font-size: 30px;
    line-height: 44px;
    color: var(--ink-light);
  }
  .contact p { margin: 0; }
  .office-line {
    position: absolute;
    left: 76px;
    right: 72px;
    top: 798px;
    display: flex;
    justify-content: space-between;
    font-family: "EB Garamond", serif;
    font-size: 13.5px;
    color: var(--ink-dark);
    white-space: nowrap;
  }
</style>
</head>
<body>
  <main class="letterhead">
    <svg class="banner" viewBox="0 0 1200 840" aria-hidden="true">
      <path class="banner-shape" d="M 46 30
        C 260 8, 470 34, 700 34
        C 880 34, 1010 8, 1142 20
        C 1132 200, 1136 500, 1128 752
        C 960 760, 820 742, 640 742
        C 440 742, 300 770, 170 770
        C 110 770, 70 740, 60 720
        C 80 520, 30 300, 62 180
        C 72 120, 40 80, 46 30 Z"/>
    </svg>

    <div class="mortarboard-art" role="img" aria-label="Illustration of a graduation mortarboard with gold tassel"></div>
    <div class="hourglass-art" role="img" aria-label="Illustration of an hourglass with green-gold sand"></div>

    <ul class="practice-areas">
      <li>Civil Litigation</li>
      <li>Family Law</li>
      <li>Crime</li>
    </ul>

    <h1 class="firm-name">KR Holloway</h1>
    <p class="firm-descriptor">Solicitors and Advocates</p>

    <div class="contact">
      <p class="contact-email">Email:&nbsp; contact@hollowaylegal.co.uk</p>
      <p class="contact-phone">Telephone: +44 (0)20 7946 0812</p>
    </div>

    <footer class="office-line">
      <span>Kestrel House 114-118 Arden Road London NW8 2QT</span>
      <span>Tel: 020 7946 0812</span>
      <span>2nd Floor, 7 Marlow Street, London, W1T 4JP</span>
    </footer>
  </main>
</body>
</html>
```